Website Graphic Layout

We are looking for someone to provide a crisp clean layout for our new website design.
The site is runs on Drupal & we like the 4 column layout
We think that the current site is a bit cluttered & could be a bit cleaner.

http://www.brovantel.org/volunteer-abroad

We like the following website as examples as they are quite clean with a large header image & sub areas to add things such as news testimonials etc

http://quindrax.com/
http://www.zorpat.com/ie/
http://harbelwing.org/
http://www.velkori.com/

Industry/Entity Type

Cleaner

```html
<!DOCTYPE html>
<html lang="en">
<head>
<meta charset="utf-8">
<title>Brovantel Volunteer Abroad</title>
<link rel="stylesheet" href="https://fonts.googleapis.com/css2?family=Ubuntu:ital,wght@0,400;0,500;0,700;1,400;1,500;1,700&display=swap">
<style>
:root{
  --blue:#1a9bd7;
  --blue-dark:#0f7fb6;
  --green:#1f8a3b;
  --green-dark:#136b2b;
  --orange:#f2a81d;
  --charcoal:#2b323b;
  --slate:#3e4753;
  --panel:#ececec;
  --panel-inner:#f6f6f6;
  --text:#333;
  --white:#fff;
}
*{margin:0;padding:0;box-sizing:border-box}
html,body{width:946px;height:1200px;overflow:hidden;background:var(--white)}
body{position:relative;font-family:"Ubuntu",sans-serif;color:var(--text)}
.abs{position:absolute}

/* header */
.brand{left:37px;top:40px;display:flex;align-items:center;gap:10px}
.brand-mark{width:58px;height:58px;border-radius:50%;background:var(--blue)}
.brand-name{font-size:30px;font-weight:700;color:var(--blue);line-height:1}
.brand-url{font-size:13px;color:var(--green);margin-top:4px}
.search{left:703px;top:27px;width:132px;height:18px;border:1px solid #ccc;background:#eee;font-size:9px;font-style:italic;color:#aaa;padding:3px 5px}
.search-go{left:852px;top:27px;width:57px;height:18px;border:1px solid #ccc;background:#eee;font-size:9px;color:#aaa;padding:3px 7px}
.social{display:flex;gap:7px}
.social span{width:26px;height:26px;border-radius:50%;background:#8fd0ee;display:block}
.header-social{left:762px;top:62px}
.user-links{right:37px;top:101px;font-size:10.5px;font-style:italic;color:var(--blue);letter-spacing:.3px}
.user-links b{font-weight:400;margin:0 6px}

.main-nav{left:37px;top:125px;width:872px;height:30px;border-top:3px solid var(--blue);border-bottom:3px solid var(--blue);display:flex;justify-content:space-between;align-items:center;font-size:11.5px;text-transform:uppercase;color:#222}
.main-nav i{font-style:normal;color:#555}

.hero{left:37px;top:155px;width:872px;height:344px;border-bottom:4px solid var(--blue);background:linear-gradient(90deg,#9a8a6c 0%,#c7b59a 35%,#d9c8b5 60%,#a9b7c3 100%)}
.hero-caption{left:443px;top:313px;width:466px;height:100px;background:rgba(244,166,22,.9);padding:4px 10px;color:var(--white);font-style:italic;font-weight:700}
.hero-caption h1{font-size:29px;font-weight:500;letter-spacing:1px;line-height:1.1}
.hero-caption h2{font-size:21px;font-weight:500;letter-spacing:.8px;line-height:1.1}
.hero-caption p{font-size:12px;line-height:17px;margin-top:6px;letter-spacing:.4px}

/* panels */
.panel-head{height:38px;color:var(--white);font-size:17px;letter-spacing:.6px;display:flex;align-items:center;justify-content:center;text-transform:uppercase}
.head-dark{background:linear-gradient(#3a414b,#1e242b)}
.head-green{background:linear-gradient(#27994a,#146a2c)}
.head-orange{background:linear-gradient(#f6b52e,#dd8f0c)}
.head-blue{background:linear-gradient(#27a7e0,#0f7fb6)}
.panel-body{background:var(--panel);overflow:hidden}
.panel-body .inner{background:var(--panel-inner);height:100%}
.panel-foot{height:22px;color:var(--white);font-size:11px;display:flex;align-items:center;justify-content:flex-end;padding-right:14px;gap:4px}
.plus{width:13px;height:13px;border-radius:50%;background:var(--white);position:relative;display:inline-block}
.plus::before,.plus::after{content:"";position:absolute;background:#444;left:3px;top:6px;width:7px;height:1.5px}
.plus::after{transform:rotate(90deg)}
.link-list{list-style:none;font-size:13.5px;color:#222}
.link-list li{display:flex;align-items:flex-start;gap:7px;line-height:23.2px}
.arrow{flex:none;width:15px;height:15px;margin-top:4px}

.sidebar{left:33px;top:532px;width:213px}
.sidebar .panel-body{height:387px;padding:14px 12px}
.sidebar .link-list{padding:12px 0 0 8px;letter-spacing:-.1px}

.welcome{left:260px;top:528px;width:426px}
.welcome h2{font-size:34px;font-style:italic;font-weight:500;color:var(--blue);padding-bottom:4px;border-bottom:1px solid #9cb;letter-spacing:.5px}
.welcome p{font-size:12.3px;line-height:19.1px;color:#444;padding:5px 0 6px;border-bottom:1px solid #9cb}
.welcome .more-link{font-size:12px;font-style:italic;color:var(--green-dark);margin-top:6px;display:flex;align-items:center;justify-content:space-between;padding-right:6px}

.finder{left:700px;top:532px;width:212px}
.finder .panel-body{height:168px;padding:8px}
.finder .inner{padding:18px 10px}
.field{display:flex;align-items:center;justify-content:space-between;font-size:11px;font-style:italic;color:#444;margin-bottom:19px}
.select{width:112px;height:20px;background:linear-gradient(#f4f4f4,#ddd);border:1px solid #ccc;font-size:10.5px;padding:3px 8px;position:relative}
.select::after{content:"";position:absolute;right:4px;top:3px;width:12px;height:12px;border-radius:50%;background:#999}
.search-btn{margin-left:auto;width:112px;height:18px;background:var(--green);color:var(--white);font-size:10.5px;font-style:italic;text-align:center;line-height:18px}
.finder-foot{height:7px;background:var(--slate)}

.news{left:255px}
.videos{left:478px}
.connect{left:700px}
.feature{top:771px;width:212px}
.feature .panel-body{height:149px;padding:6px 6px}
.feature .link-list{padding:18px 0 0 6px;font-size:13px;letter-spacing:-.15px}

.faces{display:grid;grid-template-columns:repeat(4,44px);gap:4px;padding:4px 4px}
.faces span{height:44px;display:block}
.mini-btn{height:19px;border:1px solid #bcd;background:#eef3fa;font-size:9px;color:#3b5b98;display:flex;align-items:center;justify-content:center;margin-top:3px}
.like-bar{background:var(--blue-dark);font-size:9px;font-weight:700;justify-content:center;padding:0}

/* footer */
.footer-nav{left:0;top:1022px;width:946px;height:35px;background:var(--slate);display:flex;align-items:center;padding:0 46px 0 49px;font-size:10.5px;color:#dde;text-transform:uppercase}
.footer-nav i{font-style:normal;margin:0 9px;color:#99a}
.footer-nav .share{margin-left:auto;margin-right:10px}
.footer-nav .social span{background:var(--blue)}
.footer-main{left:0;top:1057px;width:946px;height:143px;background:var(--charcoal);color:#b8bec6;font-size:9.5px}
.contact-title{left:47px;top:12px;font-size:10.5px;text-transform:uppercase}
.address{left:47px;top:30px;line-height:16.5px}
.lines{left:269px;top:30px;line-height:16.5px}
.copyright{left:40px;top:101px;display:flex;align-items:center;gap:6px;font-size:9px}
.copyright span{width:26px;height:26px;border-radius:50%;background:var(--blue)}
.newsletter{left:702px;top:26px;width:205px;height:72px;background:#3d4652;padding:4px 6px;font-size:10px;font-style:italic;color:#dde}
.nl-input{height:19px;background:#9aa0a8;color:#eee;padding:3px 6px;margin-top:3px}
.nl-row{display:flex;gap:4px}
.nl-row .nl-input{flex:1}
.nl-btn{width:60px;height:19px;margin-top:3px;background:#4f9e3c;color:#fff;text-align:center;line-height:19px}
</style>
</head>
<body>

<header>
  <div class="abs brand">
    <span class="brand-mark"></span>
    <div>
      <div class="brand-name">Brovantel Abroad</div>
      <div class="brand-url">www.brovantelabroad.ie</div>
    </div>
  </div>
  <div class="abs search">Enter search</div>
  <div class="abs search-go">GO</div>
  <div class="abs social header-social" aria-label="Social links"><span></span><span></span><span></span><span></span><span></span></div>
  <div class="abs user-links">Guest. Login<b>&gt;</b>Register<b>&gt;</b>Contact us<b>&gt;</b></div>
  <nav class="abs main-nav">
    <span>Home</span><i>|</i><span>Study Abroad</span><i>|</i><span>Volunteer Abroad</span><i>|</i><span>Development Education</span><i>|</i><span>Travel Awards</span><i>|</i><span>Visit Ireland</span><i>|</i><span>About Brovantel</span><i>|</i><span>Community</span>
  </nav>
</header>

<div class="abs hero" role="img" aria-label="Photo of two student volunteers standing with local health association staff"></div>
<div class="abs hero-caption">
  <h1>Volunteer Abroad</h1>
  <h2>Explore the world and make a difference!</h2>
  <p>Aine and Clare - Corvane University students on a Public Health internship in Jaipur, India - with the staff of the Family Health Alliance of India.</p>
</div>

<svg width="0" height="0" style="position:absolute">
  <symbol id="go-arrow" viewBox="0 0 16 16">
    <circle cx="8" cy="8" r="7" fill="none" stroke="#2a3139" stroke-width="2"/>
    <path d="M6.5 4.5 L10.5 8 L6.5 11.5 Z" fill="#2a3139"/>
  </symbol>
</svg>

<aside class="abs sidebar">
  <div class="panel-head head-dark">Volunteer Abroad</div>
  <div class="panel-body">
    <div class="inner">
      <ul class="link-list">
        <li><svg class="arrow"><use href="#go-arrow"/></svg>Countries</li>
        <li><svg class="arrow"><use href="#go-arrow"/></svg>Find your project</li>
        <li><svg class="arrow"><use href="#go-arrow"/></svg>Under-18 programme</li>
        <li><svg class="arrow"><use href="#go-arrow"/></svg>Internship Programmes</li>
        <li><svg class="arrow"><use href="#go-arrow"/></svg>Corporate Volunteering</li>
        <li><svg class="arrow"><use href="#go-arrow"/></svg>School Programme</li>
        <li><svg class="arrow"><use href="#go-arrow"/></svg>Why Brovantel?</li>
        <li><svg class="arrow"><use href="#go-arrow"/></svg>Is this for me</li>
        <li><svg class="arrow"><use href="#go-arrow"/></svg>Why Pay</li>
        <li><svg class="arrow"><use href="#go-arrow"/></svg>How do I apply</li>
        <li><svg class="arrow"><use href="#go-arrow"/></svg>Fundraising</li>
        <li><svg class="arrow"><use href="#go-arrow"/></svg>FAQ</li>
        <li><svg class="arrow"><use href="#go-arrow"/></svg>Contact us</li>
        <li><svg class="arrow"><use href="#go-arrow"/></svg>News</li>
      </ul>
    </div>
  </div>
  <div class="panel-foot head-dark">MORE <span class="plus"></span></div>
</aside>

<section class="abs welcome">
  <h2>Welcome to Brovantel</h2>
  <p>Brovantel Intercultural Learning is an Irish not for profit organisation supporting local projects across the world. Our Volunteer Abroad programme involves living, working and making a difference in a local community while learning about a new culture and gaining a new perspective on global and development issues. We offer flexible and varied voluntary work and internship opportunities all year round. Our volunteers are supported by highly qualified in-country staff with years of experience in intercultural exchanges and in supporting international volunteers.</p>
  <div class="more-link">Find out more about our approach to short term international volunteering <svg class="arrow" style="margin:0"><use href="#go-arrow"/></svg></div>
</section>

<aside class="abs finder">
  <div class="panel-head head-dark">Find you project</div>
  <div class="panel-body">
    <div class="inner">
      <div class="field">Region <span class="select">Any</span></div>
      <div class="field">Project Type <span class="select">Any</span></div>
      <div class="field">Duration <span class="select">Any</span></div>
      <div class="search-btn">Search for project</div>
    </div>
  </div>
  <div class="finder-foot"></div>
</aside>

<section class="abs feature news">
  <div class="panel-head head-green">News and Events</div>
  <div class="panel-body"><div class="inner">
    <ul class="link-list">
      <li><svg class="arrow"><use href="#go-arrow"/></svg>Sharing what I have learnt</li>
      <li><svg class="arrow"><use href="#go-arrow"/></svg>New opportunity for animal lovers in Japur, India</li>
      <li><svg class="arrow"><use href="#go-arrow"/></svg>Dose knowing a foreign language improve you?</li>
    </ul>
  </div></div>
  <div class="panel-foot head-green">MORE <span class="plus"></span></div>
</section>

<section class="abs feature videos">
  <div class="panel-head head-orange">Featured Videos</div>
  <div class="panel-body"><div class="inner">
    <ul class="link-list">
      <li><svg class="arrow"><use href="#go-arrow"/></svg>Volunteer abroad with us</li>
      <li><svg class="arrow"><use href="#go-arrow"/></svg>Volunteer in Ghana</li>
      <li><svg class="arrow"><use href="#go-arrow"/></svg>Volunteer in India</li>
      <li><svg class="arrow"><use href="#go-arrow"/></svg>Volunteer in India - Youth and 30+ Volunteer camps</li>
    </ul>
  </div></div>
  <div class="panel-foot head-orange">MORE <span class="plus"></span></div>
</section>

<section class="abs feature connect">
  <div class="panel-head head-blue">Get Connected</div>
  <div class="panel-body" style="padding:4px 6px;background:#fff">
    <div class="faces" role="img" aria-label="Grid of supporter profile photos">
      <span style="background:#8a6a55"></span><span style="background:#7c8a96"></span><span style="background:#a8604a"></span><span style="background:#6e6a5c"></span>
      <span style="background:#6d9ac8"></span><span style="background:#3c8a4a"></span><span style="background:#5a9a3a"></span><span style="background:#e8e4d8"></span>
      <span style="background:#8a7a68"></span><span style="background:#7d8aa0"></span><span style="background:#6a3a6a"></span>
      <span><div class="mini-btn" style="margin-top:0">Like</div><div class="mini-btn">Send</div></span>
    </div>
  </div>
  <div class="panel-foot like-bar">3,481 people like Brovantel Intercultural Learning</div>
</section>

<footer>
  <div class="abs footer-nav">
    <span>Home</span><i>|</i><span>Volunteer Abroad</span><i>|</i><span>Development</span><i>|</i><span>About</span><i>|</i><span>Community</span>
    <span class="share">Share this</span>
    <div class="social"><span></span><span></span><span></span><span></span><span></span></div>
  </div>
  <div class="abs footer-main">
    <div class="abs contact-title">Contact</div>
    <div class="abs address">
      <svg class="abs" style="left:-22px;top:2px" width="14" height="18" viewBox="0 0 14 18"><path d="M7 1a6 6 0 0 1 6 6c0 4-6 10-6 10S1 11 1 7a6 6 0 0 1 6-6z" fill="#8a929c"/><circle cx="7" cy="7" r="2.2" fill="#2b323b"/></svg>
      Brovantel Intercultural Learning,<br>4 Larkfield Terrace, Harbour Road,<br>Cork, County Cork, Republic of Ireland.
    </div>
    <div class="abs lines">
      <svg class="abs" style="left:-24px;top:0" width="16" height="50" viewBox="0 0 16 50">
        <rect x="4" y="0" width="8" height="13" rx="1.5" fill="none" stroke="#8a929c" stroke-width="1.5"/>
        <rect x="1" y="19" width="14" height="9" fill="none" stroke="#8a929c" stroke-width="1.5"/>
        <line x1="1" y1="22" x2="15" y2="22" stroke="#8a929c" stroke-width="1.5"/>
        <rect x="1" y="36" width="14" height="9" fill="#8a929c"/>
        <path d="M1 36 L8 41 L15 36" fill="none" stroke="#2b323b" stroke-width="1"/>
      </svg>
      850 555014<br>Fax: +353 (0)21 5550198<br>Email: info@brovantel.org
    </div>
    <div class="abs copyright"><span></span>Brovantel Intercultural Learning © copyright 2013 all rights reserved</div>
    <div class="abs newsletter">
      Get our newsletter
      <div class="nl-input">Enter your name</div>
      <div class="nl-row"><div class="nl-input">Enter your email</div><div class="nl-btn">Sign Up</div></div>
    </div>
  </div>
</footer>

</body>
</html>
```